Christmas Card Design

I would like to have a design created for a no-fold card, two sided that will be printed on card stock. I would like to have the front be four polaroid pictures (I will supply the photos that will be inserted into the polaroid pic design, with text on top of the group of four and on the bottom. I would like the header text to read "Home is where our hearts are!" and the Footer text to read "Holiday love and magic from our home to yours, The Pendletons"
I would like the back to be one polaroid in the middle. If you would like to give this project a whirl, message me and I will send the photos. Each photo will have text in the bottom of the polaroid (typically the white part of a polaroid pic.)
1) Gwen, Washington, DC 2017
2) Derek, New York City 2017
3) Marisa, Chicago 2017
4) Hugo, Worcester, MA 2017
The photo on the back will have the following text:
Ned and Pam
Wilmette, IL 2017

```html
<!DOCTYPE html>
<html lang="en">
<head>
<meta charset="utf-8">
<title>Holiday Card – The Pendletons</title>
<link rel="stylesheet" href="https://fonts.googleapis.com/css2?family=Oswald:wght@300;400;500;600;700&display=swap">
<style>
  :root {
    --page: #e8e5e0;
    --ink-blue: #2a7ea8;
    --ink-dark: #3c3c3e;
    --photo: #434548;
    --frame: #fbfaf5;
    --heart: #f2848f;
    --heart-soft: rgba(238, 130, 145, 0.55);
    --string: #fdfdfd;
    --clip: #2b2b2b;
  }
  * { box-sizing: border-box; margin: 0; padding: 0; }
  html, body { width: 1200px; height: 979px; overflow: hidden; }
  body {
    background: var(--page);
    font-family: "Oswald", sans-serif;
    position: relative;
  }
  .card {
    position: absolute;
    left: 280px;
    width: 640px;
    height: 454px;
    overflow: hidden;
    background:
      radial-gradient(ellipse 38% 45% at 55% 12%, rgba(214, 236, 196, 0.9), transparent 70%),
      radial-gradient(ellipse 30% 40% at 8% 55%, rgba(190, 222, 236, 0.9), transparent 70%),
      radial-gradient(ellipse 30% 40% at 92% 55%, rgba(196, 226, 238, 0.9), transparent 70%),
      radial-gradient(ellipse 35% 35% at 30% 95%, rgba(250, 232, 190, 0.8), transparent 70%),
      radial-gradient(ellipse 60% 60% at 50% 50%, rgba(250, 214, 205, 1), transparent 80%),
      linear-gradient(160deg, #f4c2c6 0%, #f6dad2 40%, #f2c6c8 70%, #efb3b8 100%);
    box-shadow: 0 2px 6px rgba(0,0,0,0.15);
  }
  .card--front { top: 24px; }
  .card--back  { top: 501px; }

  .soft-heart, .pin-heart { position: absolute; }
  .soft-heart { fill: var(--heart-soft); }
  .pin-heart { fill: var(--heart); z-index: 3; }

  .clothesline {
    position: absolute;
    left: 0; width: 100%;
    height: 3px;
    background: var(--string);
    border-radius: 2px;
  }

  .headline {
    position: absolute;
    color: var(--ink-blue);
    font-weight: 600;
    line-height: 1;
    font-size: 58px;
  }
  .headline .light { font-weight: 400; font-size: 46px; }
  .headline--one { left: 88px; top: 20px; }
  .headline--two { left: 197px; top: 76px; }

  .polaroid {
    position: absolute;
    background: var(--frame);
    box-shadow: 1px 2px 4px rgba(0,0,0,0.28);
    text-align: center;
    color: var(--ink-dark);
  }
  .polaroid .photo {
    background: var(--photo);
    display: block;
  }
  .polaroid .clip {
    position: absolute;
    top: -9px;
    left: 50%;
    margin-left: -7px;
  }
  .polaroid--small { width: 124px; height: 150px; padding: 8px 9px 0; }
  .polaroid--small .photo { width: 106px; height: 102px; }
  .polaroid--small .name { font-weight: 600; font-size: 19px; line-height: 1; margin-top: 4px; }
  .polaroid--small .place { font-weight: 500; font-size: 8.5px; line-height: 1.2; }

  .polaroid--gwen   { left: 35px;  top: 170px; transform: rotate(4deg); }
  .polaroid--derek  { left: 184px; top: 172px; transform: rotate(-3.5deg); }
  .polaroid--marisa { left: 341px; top: 170px; transform: rotate(0deg); }
  .polaroid--hugo   { left: 496px; top: 167px; transform: rotate(-0.5deg); }

  .sign-off {
    position: absolute;
    left: 0; width: 100%;
    text-align: center;
    color: var(--ink-blue);
    font-weight: 500;
    line-height: 1;
  }
  .sign-off--wish { top: 350px; font-size: 27px; }
  .sign-off--family { top: 389px; font-size: 34px; }

  .polaroid--large {
    left: 176px; top: 84px;
    width: 292px; height: 326px;
    padding: 16px 16px 0;
    transform: rotate(-2.5deg);
  }
  .polaroid--large .photo { width: 260px; height: 228px; }
  .polaroid--large .name { font-weight: 600; font-size: 36px; line-height: 1; margin-top: 6px; }
  .polaroid--large .place { font-weight: 600; font-size: 26px; line-height: 1.1; }
</style>
</head>
<body>
<svg width="0" height="0" style="position:absolute">
  <defs>
    <symbol id="heart" viewBox="0 0 100 90">
      <path d="M50 88 C20 65 0 48 0 26 C0 10 12 0 26 0 C38 0 46 7 50 16 C54 7 62 0 74 0 C88 0 100 10 100 26 C100 48 80 65 50 88Z"/>
    </symbol>
    <symbol id="binder-clip" viewBox="0 0 14 16">
      <rect x="1" y="7" width="12" height="8" fill="#2b2b2b"/>
      <path d="M3 8 L4 1 L10 1 L11 8" fill="none" stroke="#9a9a9a" stroke-width="1.2"/>
    </symbol>
  </defs>
</svg>

<!-- Front side -->
<section class="card card--front">
  <svg class="soft-heart" style="left:-40px;top:-30px" width="95" height="85"><use href="#heart"/></svg>
  <svg class="soft-heart" style="left:500px;top:-20px;transform:rotate(-20deg)" width="180" height="160"><use href="#heart"/></svg>
  <svg class="soft-heart" style="left:50px;top:385px;transform:rotate(-15deg)" width="120" height="110"><use href="#heart"/></svg>
  <svg class="soft-heart" style="left:580px;top:395px;transform:rotate(-15deg)" width="90" height="80"><use href="#heart"/></svg>

  <h1 class="headline headline--one">Home <span class="light">is</span> where</h1>
  <h1 class="headline headline--two">our hearts <span class="light">are</span>!</h1>

  <div class="clothesline" style="top:153px;transform:rotate(0.5deg)"></div>

  <figure class="polaroid polaroid--small polaroid--gwen">
    <svg class="clip" width="14" height="16"><use href="#binder-clip"/></svg>
    <div class="photo" role="img" aria-label="Photo of Gwen"></div>
    <figcaption><div class="name">Gwen,</div><div class="place">Washington, DC 2017</div></figcaption>
  </figure>
  <figure class="polaroid polaroid--small polaroid--derek">
    <svg class="clip" width="14" height="16"><use href="#binder-clip"/></svg>
    <div class="photo" role="img" aria-label="Photo of Derek"></div>
    <figcaption><div class="name">Derek,</div><div class="place">New York City 2017</div></figcaption>
  </figure>
  <figure class="polaroid polaroid--small polaroid--marisa">
    <svg class="clip" width="14" height="16"><use href="#binder-clip"/></svg>
    <div class="photo" role="img" aria-label="Photo of Marisa"></div>
    <figcaption><div class="name">Marisa,</div><div class="place">Chicago 2017</div></figcaption>
  </figure>
  <figure class="polaroid polaroid--small polaroid--hugo">
    <svg class="clip" width="14" height="16"><use href="#binder-clip"/></svg>
    <div class="photo" role="img" aria-label="Photo of Hugo"></div>
    <figcaption><div class="name">Hugo,</div><div class="place">Worcester, MA 2017</div></figcaption>
  </figure>

  <svg class="pin-heart" style="left:27px;top:152px;transform:rotate(-15deg)" width="36" height="32"><use href="#heart"/></svg>
  <svg class="pin-heart" style="left:279px;top:157px;transform:rotate(10deg)" width="36" height="32"><use href="#heart"/></svg>
  <svg class="pin-heart" style="left:338px;top:257px;transform:rotate(-15deg)" width="36" height="32"><use href="#heart"/></svg>
  <svg class="pin-heart" style="left:485px;top:160px;transform:rotate(-15deg)" width="34" height="32"><use href="#heart"/></svg>

  <p class="sign-off sign-off--wish">Holiday love and magic from our home to yours,</p>
  <p class="sign-off sign-off--family">The Pendletons</p>
</section>

<!-- Back side -->
<section class="card card--back">
  <svg class="soft-heart" style="left:-20px;top:-15px" width="80" height="70"><use href="#heart"/></svg>
  <svg class="soft-heart" style="left:-25px;top:345px;transform:rotate(-12deg)" width="180" height="160"><use href="#heart"/></svg>
  <svg class="soft-heart" style="left:575px;top:390px;transform:rotate(-15deg)" width="100" height="90"><use href="#heart"/></svg>

  <div class="clothesline" style="top:36px;transform:rotate(1.5deg)"></div>

  <figure class="polaroid polaroid--large">
    <div class="photo" role="img" aria-label="Photo of Ned and Pam"></div>
    <figcaption><div class="name">Ned and Pam</div><div class="place">Wilmette, IL 2017</div></figcaption>
  </figure>

  <svg class="pin-heart" style="left:145px;top:62px;transform:rotate(-20deg)" width="56" height="52"><use href="#heart"/></svg>
  <svg class="pin-heart" style="left:427px;top:280px;transform:rotate(-10deg)" width="64" height="56"><use href="#heart"/></svg>
</section>
</body>
</html>
```